Ledgerwise Reach - B2B Demand Generation Website Project

We need a fully functional website for www.ledgerwisereach.example. We are a B2B Demand Generation company, based in London, working with companies such as QRT, VKD, Norvex, Brindlow, Tarvo generating them sales leads for their sales teams. We run this through digital marketing newsletter promotions and have a network of websites. Content syndication, data, demand generation, online marketing. Our logo has just been redone (attached) and we have a holding page already which i would like to use the style / colours. Our logo is bright and vibrant but i dont want the site to be a rainbow. We are expensive, classy, professorial, B2B, intelligent.

Home
About Us
Our Services
Prospora & QA Technology
Intent Data
Testimonials
Contact Us
Updates

Target Market(s)

B2B Marketers (QRT, Velquarion, Tarvo, VKD, Opal Reach, Driftmoor, Harlow Quantis, Technology Companies, Data Companies, Marketing Teams, Tumbleden.

Industry/Entity Type

Marketing

Coding

Coded - Design and coding required

Number of Pages Required

5+ page

Font styles to use
Sans Serif

Requirements
Must have
• Home
About Us
Our Services
Prospora & QA Technology
Intent Data
Testimonials
Contact Us

Simple Pages.

Look classy, intelligent, data experts. I like the video homepages were the image moves at the top. Very soft animation.
Nice to have
• Websites i like:

https://www.vkd.example/
https://www.brevantor.example/
https://www.plumfieldsites.example.co.uk/

Ledgerwise Reach - The Demand Generation Company
Should not have
• Glimpsevault crap images

```html
<!DOCTYPE html>
<html lang="en">
<head>
<meta charset="utf-8">
<title>Ledgerwise Reach - The Demand Generation Company</title>
<link rel="stylesheet" href="https://fonts.googleapis.com/css2?family=Montserrat:wght@400;500&family=Open+Sans:wght@400;500&display=swap">
<style>
  :root {
    --brand-red: #d1262d;
    --brand-blue: #1d5a9c;
    --page-bg: #ffffff;
    --hero-deep: #02070d;
    --hero-mid: #0a3f6e;
    --hero-glow: #5fb6e6;
    --hero-text: #ffffff;
  }
  * { margin: 0; padding: 0; box-sizing: border-box; }
  html, body {
    width: 1200px;
    height: 1200px;
    overflow: hidden;
    background: var(--page-bg);
  }
  a { text-decoration: none; color: inherit; }
  .site {
    position: relative;
    width: 1200px;
    height: 1200px;
  }
  .brand {
    position: absolute;
    left: 141px;
    top: 22px;
    width: 216px;
    display: block;
    text-align: center;
    text-decoration: none;
  }
  .brand-dot {
    display: block;
    width: 60px;
    height: 60px;
    margin: 0 0 6px 77px;
    border-radius: 50%;
    background: var(--brand-red);
  }
  .brand-name {
    display: block;
    font-family: "Montserrat", sans-serif;
    font-weight: 400;
    font-size: 26px;
    letter-spacing: -0.3px;
    line-height: 30px;
    color: var(--brand-red);
    white-space: nowrap;
  }
  .brand-tagline {
    display: block;
    font-family: "Montserrat", sans-serif;
    font-weight: 500;
    font-size: 8.5px;
    line-height: 12px;
    color: var(--brand-blue);
    margin-top: 2px;
    white-space: nowrap;
  }
  .main-nav {
    position: absolute;
    left: 139px;
    top: 179px;
    display: flex;
    gap: 14px;
    list-style: none;
    font-family: "Open Sans", sans-serif;
    font-weight: 500;
    font-size: 18px;
    line-height: 26px;
    color: var(--brand-red);
    white-space: nowrap;
  }
  .main-nav a { color: inherit; text-decoration: none; }
  .hero {
    position: absolute;
    left: 21px;
    top: 238px;
    width: 1179px;
    height: 675px;
    overflow: hidden;
  }
  .hero-visual {
    position: absolute;
    inset: 0;
    background:
      radial-gradient(ellipse 55% 60% at 62% 45%, var(--hero-glow) 0%, rgba(40,130,190,0.55) 35%, rgba(6,40,70,0) 75%),
      radial-gradient(ellipse 35% 40% at 25% 50%, var(--hero-deep) 0%, rgba(2,7,13,0.6) 50%, rgba(2,7,13,0) 100%),
      linear-gradient(100deg, var(--hero-mid) 0%, #1a6aa5 45%, #0b2c4a 78%, var(--hero-deep) 100%);
  }
  .hero-caption {
    position: absolute;
    left: 961px;
    top: 516px;
    font-family: "Montserrat", sans-serif;
    color: var(--hero-text);
  }
  .hero-brand {
    display: block;
    font-weight: 500;
    font-size: 20px;
    line-height: 28px;
    color: var(--brand-red);
    white-space: nowrap;
  }
  .hero-tagline {
    display: block;
    font-weight: 400;
    font-size: 23px;
    line-height: 29px;
    letter-spacing: 0.6px;
  }
</style>
</head>
<body>
<div class="site">
  <header>
    <a class="brand" href="#">
      <span class="brand-dot"></span>
      <span class="brand-name">ledgerwisereach</span>
      <span class="brand-tagline">The Demand Generation Company</span>
    </a>
    <ul class="main-nav">
      <li><a href="#">Home</a></li>
      <li><a href="#">About Us</a></li>
      <li><a href="#">Our Services</a></li>
      <li><a href="#">Prospora &amp; QA Technology</a></li>
      <li><a href="#">Intent Data</a></li>
      <li><a href="#">Testimonials</a></li>
      <li><a href="#">Contact Us</a></li>
    </ul>
  </header>
  <section class="hero">
    <div class="hero-visual" role="img" aria-label="Abstract tunnel of glowing blue light dots spiralling into a dark centre"></div>
    <div class="hero-caption">
      <span class="hero-brand">ledgerwisereach</span>
      <span class="hero-tagline">The Demand<br>Generation<br>Company</span>
    </div>
  </section>
</div>
</body>
</html>
```